VaultMeridan Business Card Re-Design

VaultMeridan is a specialized information security company that applies its proven methodology of security Assessment, Development, Integration and Training (A-D-I-T) to provide cyber security services in the areas of Data Protection, Network Defense and Compliance. We need the current business card re-designed to properly scale the fonts and possibly rearranging some elements (icons, lettering, etc.) to make the card more appealing to the eye. The card should have the logo that is on the web site (www.vaultmeridan-example.com). We would like ideas for both a black card (black background) and a white card (white background). We prefer rounded corners to help the card stand out but are open to all ideas. FYI: VaultMeridan's slogan is "...Protecting What Matters Most".

Target Market(s)

#1 US Government Contracting Companies, #2 Commercial Companies, #3 Gen. Public.

Industry/Entity Type

Business

Contact Information for Business Card

See Description; open to the use of different fonts.

Font styles to use
Sans Serif

Colors
000000
ec1f27
ffffff

Requirements
Must have
• Company logo on web site, rounded corners, list of company offerings on the back of the card.
Nice to have
• Icons
Should not have
• none

```html
<!DOCTYPE html>
<html lang="en">
<head>
<meta charset="utf-8">
<title>VaultMeridan Business Card</title>
<link rel="stylesheet" href="https://fonts.googleapis.com/css2?family=Open+Sans:wght@300;400;600;700&family=Lato:wght@400&display=swap">
<style>
  :root {
    --black: #000000;
    --card: #0b0b0b;
    --card-top: #1c1c1c;
    --red: #ec1f27;
    --white: #ffffff;
    --stage: #5b5b5b;
  }
  * { margin: 0; padding: 0; box-sizing: border-box; }
  html, body { width: 1200px; height: 1000px; overflow: hidden; }
  body {
    position: relative;
    background: var(--stage);
    font-family: "Open Sans", Verdana, sans-serif;
    color: var(--white);
  }
  .card {
    position: absolute;
    border-radius: 12px;
    overflow: hidden;
    background: var(--card);
  }
  /* Front */
  .card-front { left: 121px; top: 110px; width: 620px; height: 342px; }
  .brand { position: absolute; display: flex; align-items: center; gap: 12px; }
  .brand-mark { width: 18px; height: 18px; background: var(--red); }
  .brand-name { font-weight: 600; font-size: 38px; letter-spacing: 3px; color: var(--white); line-height: 1; }
  .brand-sub { position: absolute; font-weight: 300; font-size: 17px; letter-spacing: 1.5px; color: var(--white); }
  .card-front .brand { left: 26px; top: 32px; }
  .card-front .brand-sub { left: 82px; top: 90px; }
  .person { position: absolute; left: 26px; top: 158px; }
  .person-name { font-family: "Open Sans", sans-serif; font-weight: 700; font-size: 24px; color: var(--red); }
  .person-role { font-family: "Open Sans", sans-serif; font-weight: 700; font-size: 14px; color: var(--white); margin-left: 6px; }
  .person-creds { font-family: "Open Sans", sans-serif; font-size: 12px; margin-top: -4px; }
  .contact { position: absolute; left: 26px; top: 226px; list-style: none; font-family: "Open Sans", sans-serif; font-size: 13.5px; }
  .contact li { display: flex; align-items: flex-start; gap: 8px; margin-bottom: 7px; line-height: 18px; }
  .contact svg { width: 14px; height: 14px; margin-top: 2px; flex: none; }
  .contact .stack { line-height: 19px; }
  .contact li.email svg { margin-top: 10px; }
  .address { position: absolute; left: 394px; top: 262px; font-family: "Open Sans", sans-serif; font-size: 12px; line-height: 15px; white-space: nowrap; }
  .address-pin { position: absolute; left: 580px; top: 273px; width: 16px; height: 22px; }
  .web-band {
    position: absolute; left: 0; bottom: 0; width: 100%; height: 27px;
    background: var(--red); text-align: center;
    font-family: "Open Sans", sans-serif; font-size: 13px; line-height: 26px;
  }
  /* Back */
  .card-back {
    left: 477px; top: 548px; width: 613px; height: 340px;
    background: radial-gradient(ellipse at 50% 20%, var(--card-top), var(--card) 70%);
  }
  .side-strip { position: absolute; top: 32px; width: 10px; height: 285px; background: var(--red); }
  .side-strip.left { left: 0; border-radius: 0 8px 8px 0; }
  .side-strip.right { right: 0; border-radius: 8px 0 0 8px; }
  .card-back .brand { left: 160px; top: 34px; }
  .card-back .brand-sub { left: 204px; top: 87px; font-size: 15px; }
  .services {
    position: absolute; left: 20px; top: 162px; width: 573px;
    text-align: center; white-space: nowrap;
    font-family: "Open Sans", sans-serif; font-size: 10.6px; line-height: 24.6px; color: var(--white);
  }
  .dot { display: inline-block; width: 6px; height: 6px; border-radius: 50%; background: var(--red); margin: 0 4px 1px; }
  .slogan {
    position: absolute; left: 0; top: 300px; width: 100%;
    display: flex; justify-content: center; align-items: center; gap: 12px;
    font-family: "Lato", sans-serif; font-size: 14.5px; color: var(--white);
  }
  .slogan-rule { width: 42px; height: 2px; background: var(--red); }
</style>
</head>
<body>

<section class="card card-front" aria-label="Business card front">
  <div class="brand"><span class="brand-mark"></span><span class="brand-name">VaultMeridan</span></div>
  <div class="brand-sub">INFORMATION SECURITY</div>

  <div class="person">
    <div><span class="person-name">Marcus Hale,</span><span class="person-role">President - CEO</span></div>
    <div class="person-creds">MS, BS Eng</div>
  </div>

  <ul class="contact">
    <li>
      <svg viewBox="0 0 14 14"><circle cx="7" cy="7" r="6" fill="none" stroke="#ec1f27" stroke-width="1.2"/><path d="M4.6 4.2l1.2-.4.8 1.6-.7.6c.4.9 1 1.5 1.9 1.9l.6-.7 1.6.8-.4 1.2c-2.7-.2-4.8-2.3-5-5z" fill="#ec1f27"/></svg>
      <span>555-014-2207</span>
    </li>
    <li>
      <svg viewBox="0 0 14 14"><rect x="3.5" y="0.8" width="7" height="12.4" rx="1.4" fill="none" stroke="#ec1f27" stroke-width="1.3"/><circle cx="7" cy="11" r="0.8" fill="#ec1f27"/></svg>
      <span>555-019-3348</span>
    </li>
    <li class="email">
      <svg viewBox="0 0 14 14"><rect x="0.8" y="2.6" width="12.4" height="8.8" fill="none" stroke="#ec1f27" stroke-width="1.2"/><path d="M1 3l6 5 6-5" fill="none" stroke="#ec1f27" stroke-width="1.2"/></svg>
      <span class="stack">info@vaultmeridan-example.com<br>mhale@vaultmeridan-example.com</span>
    </li>
  </ul>

  <div class="address">VaultMeridan, Inc<br>1420 Harbor Ridge Rd.Suite 210<br>Easton, Maryland 21601</div>
  <svg class="address-pin" viewBox="0 0 16 22" aria-hidden="true"><path d="M8 1a7 7 0 0 0-7 7c0 5 7 13 7 13s7-8 7-13a7 7 0 0 0-7-7z" fill="none" stroke="#ec1f27" stroke-width="1.6"/><circle cx="8" cy="8" r="2.4" fill="#ec1f27"/></svg>

  <div class="web-band">www.vaultmeridan-example.com</div>
</section>

<section class="card card-back" aria-label="Business card back">
  <div class="side-strip left"></div>
  <div class="side-strip right"></div>
  <div class="brand"><span class="brand-mark"></span><span class="brand-name">VaultMeridan</span></div>
  <div class="brand-sub">INFORMATION SECURITY</div>

  <p class="services">
    Secure Cloud &amp; Hybrid Stack Design<span class="dot"></span>Network Intrusion Testing &amp; Defense<br>
    Adversary Simulation<span class="dot"></span>Data Center Modernization<span class="dot"></span>Secure Virtual Platforms<span class="dot"></span>Sensitive<br>
    Multi-Domain Solutions<span class="dot"></span>Insider Threat &amp; Espionage Data Protection<span class="dot"></span>Compliance &amp;<br>
    Audit Readiness<span class="dot"></span>Protected Wireless Networks<span class="dot"></span>Security Training, Review &amp; Integration<br>
    Security Domain Specialists<span class="dot"></span>Leadership Risk Strategy Advising<span class="dot"></span>Data Encryption/Privacy
  </p>

  <div class="slogan"><span class="slogan-rule"></span><span>Protecting What Matters Most</span><span class="slogan-rule"></span></div>
</section>

</body>
</html>
```